Design a first class flights website. need php and html

I am looking for someone to redesign my site. I have partnerships with velmora and skyvantrix.
The website is www.zentriq9p.com. Have a looking, it is a very simple site and who ever wins i have another site i need designing too.
I am looking for someone that can do it in chinese and cantonese too.

```html
<!DOCTYPE html>
<html lang="en">
<head>
<meta charset="utf-8">
<title>Zentriq – Luxury for Low Prices</title>
<link href="https://fonts.googleapis.com/css2?family=Oswald:wght@300;400;500&family=Arimo:wght@400;700&display=swap" rel="stylesheet">
<style>
  :root {
    --blue: #1d5fbf;
    --blue-dark: #154a9c;
    --blue-bright: #1e90e0;
    --nav-dark: #1b1b1b;
    --text: #333;
    --muted: #666;
    --line: #dcdcdc;
    --page-bg: #f1f2f4;
    --footer: #333;
  }
  * { box-sizing: border-box; margin: 0; padding: 0; }
  html, body { width: 1059px; height: 1200px; overflow: hidden; }
  body { background: var(--page-bg); font-family: "Arimo", Arial, sans-serif; color: var(--text); position: relative; }
  .page { position: absolute; left: 118px; top: 20px; width: 824px; height: 1133px; background: #fff; }
  .abs { position: absolute; }

  .brand { left: 15px; top: 16px; }
  .brand-row { display: flex; align-items: center; gap: 10px; }
  .brand-mark { width: 22px; height: 22px; background: var(--text); display: block; }
  .brand-name { font-family: "Arimo", sans-serif; font-weight: 700; font-size: 28px; line-height: 34px; color: var(--text); }
  .brand-tag { font-size: 10.5px; font-weight: 700; color: #888; margin-top: 6px; }
  .lang { right: 25px; top: 20px; font-size: 11px; color: var(--blue); }
  .search { left: 556px; top: 48px; width: 247px; height: 33px; background: var(--blue); padding: 6px 9px; display: flex; gap: 8px; }
  .search-field { flex: 1; background: #fff; font-size: 10px; color: #aaa; padding: 5px 8px; }
  .search-btn { background: var(--blue-dark); color: #fff; font-size: 10.5px; font-weight: 700; padding: 5px 9px; }

  .nav { left: 15px; top: 81px; width: 788px; height: 31px; background: linear-gradient(#333, var(--nav-dark)); display: flex; align-items: center; }
  .nav a { color: #fff; text-decoration: none; font-size: 11px; font-weight: 700; padding: 0 16px; line-height: 31px; border-right: 1px solid #444; }
  .social { margin-left: auto; margin-right: 12px; display: flex; gap: 4px; }
  .social span { width: 17px; height: 17px; background: #3a6fc4; display: block; }

  .hero { left: 15px; top: 122px; width: 788px; height: 373px; overflow: hidden; }
  .hero-photo { width: 100%; height: 345px; background: linear-gradient(180deg, #2f66c4 0%, #5c95e0 45%, #c7d9ee 62%, #b88b6e 78%, #a77a5e 100%); }
  .hero-dots { height: 28px; background: #d9d3cf; display: flex; justify-content: center; align-items: center; gap: 6px; }
  .hero-dots i { width: 10px; height: 10px; border-radius: 50%; background: #aaa; }
  .hero-dots i:first-child { background: var(--blue); }
  .hero-title { left: 27px; top: 42px; font-family: "Oswald", sans-serif; font-weight: 300; font-size: 28px; line-height: 35px; color: #fff; }
  .quick { left: 522px; top: 33px; width: 250px; height: 279px; background: rgba(255,255,255,0.3); padding: 12px 10px; }
  .quick h2 { font-weight: 400; font-size: 20px; color: #fff; margin-bottom: 10px; }
  .quick .field { background: #fff; height: 24px; margin-bottom: 10px; font-size: 10px; color: #777; padding: 6px 5px; }
  .quick .field.tall { height: 72px; }
  .btn-blue { background: var(--blue); color: #fff; font-size: 11px; font-weight: 700; padding: 9px 8px; display: inline-block; border-radius: 2px; }

  .features { left: 15px; top: 510px; width: 788px; display: flex; gap: 10px; }
  .feature { flex: 1; height: 94px; background: var(--blue); border-bottom: 4px solid var(--blue-dark); color: #fff; font-family: "Oswald", sans-serif; font-weight: 300; font-size: 19px; line-height: 22px; padding: 9px 11px; }

  .section-title { font-family: "Oswald", sans-serif; font-weight: 400; font-size: 18px; color: var(--blue); padding-bottom: 6px; border-bottom: 1px solid var(--line); }
  .about { left: 15px; top: 622px; width: 458px; }
  .about p { font-size: 10px; line-height: 15px; color: var(--muted); margin-top: 10px; }
  .btn-dark { display: inline-block; background: #1a1a1a; color: #fff; font-size: 11px; font-weight: 700; padding: 7px 15px; border-radius: 14px; margin-top: 10px; box-shadow: 0 2px 3px rgba(0,0,0,.3); }
  .contact { left: 15px; top: 780px; width: 458px; }
  .step { display: flex; gap: 8px; margin-top: 16px; font-size: 10.5px; font-weight: 700; line-height: 13px; }
  .step b { flex: none; width: 24px; height: 24px; border-radius: 50%; background: var(--blue-bright); color: #fff; font-size: 14px; text-align: center; line-height: 24px; }
  .price { display: inline-block; margin: 18px 0 0 31px; background: var(--blue); border-bottom: 3px solid var(--blue-dark); color: #fff; font-size: 14px; padding: 13px 10px; }

  .reserve { left: 512px; top: 627px; width: 290px; height: 388px; border: 2px solid var(--blue-bright); border-radius: 6px; overflow: hidden; }
  .reserve h2 { background: var(--blue-bright); color: #fff; font-family: "Oswald", sans-serif; font-weight: 300; font-size: 19px; padding: 7px 10px; }
  .reserve .fields { padding: 8px 9px; }
  .reserve .field { border: 1px solid var(--line); height: 28px; font-size: 10px; padding: 8px 5px; margin-bottom: 8px; }
  .reserve .field.tall { height: 87px; }
  .req { color: #d22; }
  .submit { display: flex; align-items: center; gap: 8px; width: 129px; margin: 4px auto 0; background: var(--blue); color: #fff; font-size: 19px; padding: 8px 14px; border-radius: 3px; }

  .partners { left: 15px; top: 1045px; width: 788px; height: 76px; background: #f0f0f0; display: flex; align-items: center; gap: 10px; padding: 0 30px; }
  .partner { flex: 1; height: 47px; background: #fff; border: 1px solid #ddd; font-size: 11px; font-weight: 700; color: #555; display: flex; align-items: center; justify-content: center; text-align: center; }

  .footer { left: 0; top: 1153px; width: 1059px; height: 47px; background: var(--footer); color: #fff; font-size: 10.5px; }
  .footer .copy { position: absolute; left: 135px; top: 18px; }
  .footer .links { position: absolute; right: 135px; top: 18px; }
</style>
</head>
<body>
<div class="page">
  <div class="abs brand">
    <div class="brand-row"><span class="brand-mark"></span><span class="brand-name">Zentriq</span></div>
    <div class="brand-tag">LUXURY FOR LOW PRICES</div>
  </div>
  <div class="abs lang">中文 &nbsp;|&nbsp; English</div>
  <div class="abs search"><div class="search-field">Search for airline...</div><div class="search-btn">Search</div></div>

  <nav class="abs nav">
    <a>HOME</a><a>ABOUT US</a><a>SAMPLE PRICES</a><a>BOOK HOTELS ONLINE</a><a>SERVICES</a><a>ENQUIRY</a><a>CONTACT US</a>
    <div class="social"><span></span><span></span></div>
  </nav>

  <section class="abs hero">
    <div class="hero-photo" role="img" aria-label="Photo of a passenger jet landing on a runway under a blue sky"></div>
    <div class="hero-dots"><i></i><i></i><i></i></div>
    <h1 class="abs hero-title">We can fly you from any<br>destination to any city Worldwide</h1>
    <form class="abs quick">
      <h2>Quick Enquiry</h2>
      <div class="field">Full Name:</div>
      <div class="field">Email ID:</div>
      <div class="field">Contact No.:</div>
      <div class="field tall">Query:</div>
      <span class="btn-blue">SEND FORM</span>
    </form>
  </section>

  <div class="abs features">
    <div class="feature">We deal with all major airlines from Meridian Air to Harbourline Pacific and Albion Airways etc</div>
    <div class="feature">We can fly you from any destination to any city Worldwide</div>
    <div class="feature">You fly business or first class saving 1000s</div>
  </div>

  <section class="abs about">
    <h2 class="section-title">ABOUT COMPANY</h2>
    <p>Lorem ipsum dolor sit amet conse ctetur adipisicing elit, sed do eiusmod tempor incididunt ut labore et dolore magna aliqua. Ut enim ad minim veniam, quis nostrud exercitation ullamco laboris.</p>
    <p>Lorem ipsum dolor sit amet conse ctetur adipisicing elit, sed do eiusmod tempor incididunt ut labore et dolore magna aliqua. Ut enim ad minim veniam, quis nostrud exercitation ullamco laboris.</p>
    <span class="btn-dark">Read More</span>
  </section>

  <section class="abs contact">
    <h2 class="section-title">CONTACT DETAILS</h2>
    <div class="step"><b>1</b><span style="padding-top:5px">Submit your flight quotation request.</span></div>
    <div class="step"><b>2</b><span>One of our highly experienced travel advisors will respond with all the discount options within a maximum of 12 hours.</span></div>
    <div class="step"><b>2</b><span>Please bear in mind that our special deals are ONLY for International First &amp; Business class. We cannot attempt to be cheaper unless the round-trip retail price is at least</span></div>
    <span class="price">$3,000 USD / €2,300 EUR / £2,000 GBP.</span>
  </section>

  <form class="abs reserve">
    <h2>Reserve Your Discount Luxury Seat</h2>
    <div class="fields">
      <div class="field">Your Name:</div>
      <div class="field">Email Address:</div>
      <div class="field">Please verify your email: <span class="req">*</span></div>
      <div class="field">Country: <span class="req">*</span></div>
      <div class="field">Phone / Mobile Number: <span class="req">*</span></div>
      <div class="field tall">Memo</div>
      <div class="submit">SUBMIT
        <svg width="22" height="22" viewBox="0 0 22 22"><circle cx="11" cy="11" r="10" fill="#fff"/><path d="M9 6l5 5-5 5" fill="none" stroke="#1d5fbf" stroke-width="2.5"/></svg>
      </div>
    </div>
  </form>

  <div class="abs partners">
    <div class="partner">Jade Sky Air</div>
    <div class="partner">Albion Airways</div>
    <div class="partner">Transverse Airlines</div>
    <div class="partner">Aerolis</div>
    <div class="partner">Dunecrest</div>
    <div class="partner">Harbourline Pacific</div>
  </div>
</div>

<footer class="abs footer">
  <span class="copy">Copyright 2013 - Zentriq - All rights reserved.</span>
  <span class="links">Home &nbsp;|&nbsp; About Us &nbsp;|&nbsp; Services &nbsp;|&nbsp; Enquiry &nbsp;|&nbsp; Contact Us</span>
</footer>
</body>
</html>
```